Create Label for Jojoba Oil and Argan Oil

We already have a logo design and we tried editing a label for pure Jojoba and Argan oils. We would like to have someone do two designs for our label.

We want people to distinguish between the two bottles of Argan and Jojoba but they must be on the same theme.

Also, we would like to have an elegant feel to the label.

Logo Design is attached in the files and some pictures of the bottles. The current labels are just their because we tried coming up with our own labels. You have freedom to change the look.

Target Market(s)

adult women and men

Industry/Entity Type

Cosmetic

Requirements
Must have
• The container uses Frosted glass as shown in pictures attached.
• Please do not change the shape of the Logo; although you have freedom to change the color.
• Designs must contain the following:
• For our Jojoba Oil:
• -- 100% Pure Jojoba Oil
• -- Face, Body & Hair
• -- 118 mL
• -- www.varolune.com
• -- Ingredient: Simmondsia Chinensis (Jojoba) Seed Oil
• -- For external use only
• -- must fit within 3" X 2.5" HIGH-GLOSS PAPER
• For our Argan Oil:
• -- 100% Pure Moroccan Argan Oil
• -- Face, Body & Hair
• -- 50 mL
• -- www.varolune.com
• -- Ingredient: Argania Spinosa (Argan) Kernel Oil
• -- must fit within 3.25" X 1.75" HIGH-GLOSS PAPER
Nice to have
• Must be good printed on High Gloss Paper and seen on a Website.

```html
<!DOCTYPE html>
<html lang="en">
<head>
<meta charset="utf-8">
<title>Varolune Oil Labels</title>
<link rel="stylesheet" href="https://fonts.googleapis.com/css2?family=Comfortaa:wght@400&family=Great+Vibes&family=Montserrat:wght@400;500&display=swap">
<style>
  :root {
    --page: #ffffff;
    --label: #f6f6f6;
    --ink: #1e1e1e;
    --muted: #555555;
    --jojoba: #2fa84a;
    --argan: #f08a1c;
  }
  html, body {
    margin: 0;
    padding: 0;
    overflow: hidden;
    background: var(--page);
  }
  .canvas {
    position: relative;
    width: 1200px;
    height: 857px;
    background: var(--page);
    overflow: hidden;
  }
  .label {
    position: absolute;
    background: var(--label);
    box-shadow: 0 6px 24px rgba(0,0,0,0.08);
    box-sizing: border-box;
    border-bottom: 6px solid var(--accent);
    font-family: "Montserrat", sans-serif;
  }

  /* 3" x 2.5" label */
  .label--jojoba {
    --accent: var(--jojoba);
    left: 140px;
    top: 250px;
    width: 420px;
    height: 350px;
    padding: 18px 20px 10px;
    display: flex;
    flex-direction: column;
    align-items: center;
  }
  /* 3.25" x 1.75" label */
  .label--argan {
    --accent: var(--argan);
    left: 610px;
    top: 355px;
    width: 455px;
    height: 245px;
    padding: 14px 18px 10px;
  }

  .brand {
    display: flex;
    flex-direction: column;
    align-items: center;
    gap: 5px;
  }
  .brand__dot {
    border-radius: 50%;
    border: 3px solid var(--accent);
    box-sizing: border-box;
  }
  .brand__name {
    font-family: "Comfortaa", sans-serif;
    color: var(--accent);
    line-height: 1;
  }
  .purity {
    background: var(--accent);
    color: #fff;
    font-weight: 500;
    display: flex;
    align-items: baseline;
    gap: 6px;
    line-height: 1.2;
  }
  .purity__script {
    font-family: "Great Vibes", cursive;
    font-weight: 400;
  }
  .origin {
    letter-spacing: 3px;
    color: var(--muted);
  }
  .product {
    font-family: "Great Vibes", cursive;
    color: var(--ink);
    line-height: 1.05;
  }
  .uses {
    color: var(--muted);
    letter-spacing: 0.5px;
  }
  .ingredient, .caution {
    color: var(--muted);
    text-align: center;
  }
  .caution {
    letter-spacing: 1px;
    text-transform: uppercase;
  }
  .footer {
    display: flex;
    justify-content: space-between;
    align-items: flex-end;
  }
  .footer__web {
    font-size: 10px;
    color: var(--muted);
  }
  .footer__volume {
    color: var(--ink);
  }

  /* Jojoba sizing */
  .label--jojoba .brand__dot { width: 32px; height: 32px; }
  .label--jojoba .brand__name { font-size: 28px; }
  .label--jojoba .purity { margin-top: 6px; font-size: 14px; padding: 1px 12px; }
  .label--jojoba .purity__script { font-size: 18px; }
  .label--jojoba .product { font-size: 44px; margin-top: 2px; }
  .label--jojoba .uses { font-size: 10px; }
  .label--jojoba .botanical {
    margin-top: 6px;
    width: 220px;
    height: 66px;
    border-radius: 34px 8px 34px 8px;
    background: linear-gradient(135deg, #d9efd9, #9fcf9a);
  }
  .label--jojoba .ingredient { margin-top: 6px; font-size: 9px; }
  .label--jojoba .caution { margin-top: 3px; font-size: 8px; }
  .label--jojoba .footer { margin-top: auto; width: 100%; }
  .label--jojoba .footer__volume { font-size: 16px; }

  /* Argan sizing: text column left, botanical right */
  .label--argan .text-column {
    position: absolute;
    left: 18px;
    top: 12px;
    width: 270px;
    display: flex;
    flex-direction: column;
    align-items: center;
  }
  .label--argan .brand__dot { width: 24px; height: 24px; border-width: 2px; }
  .label--argan .brand__name { font-size: 22px; }
  .label--argan .purity { margin-top: 4px; font-size: 12px; padding: 0 10px; }
  .label--argan .purity__script { font-size: 15px; }
  .label--argan .origin { margin-top: 3px; font-size: 8px; }
  .label--argan .product { font-size: 36px; }
  .label--argan .uses { font-size: 9px; }
  .label--argan .ingredient { margin-top: 5px; font-size: 8px; }
  .label--argan .botanical {
    position: absolute;
    right: 18px;
    top: 40px;
    width: 140px;
    height: 120px;
    border-radius: 50px 8px 50px 8px;
    background: linear-gradient(135deg, #eef5e6, #a9d39a);
  }
  .label--argan .footer {
    position: absolute;
    left: 18px;
    right: 18px;
    bottom: 10px;
  }
  .label--argan .footer__volume { font-size: 15px; }
</style>
</head>
<body>
<main class="canvas">

  <section class="label label--jojoba">
    <div class="brand">
      <span class="brand__dot"></span>
      <span class="brand__name">Varolune</span>
    </div>
    <div class="purity">100% <span class="purity__script">Pure</span></div>
    <div class="product">Jojoba Oil</div>
    <div class="uses">Face, Body &amp; Hair</div>
    <div class="botanical" role="img" aria-label="Botanical drawing of a jojoba branch with leaves and seeds"></div>
    <div class="ingredient">Ingredient: Simmondsia Chinensis (Jojoba) Seed Oil</div>
    <div class="caution">For external use only</div>
    <div class="footer">
      <span class="footer__web">www.varolune.com</span>
      <span class="footer__volume">118 mL</span>
    </div>
  </section>

  <section class="label label--argan">
    <div class="text-column">
      <div class="brand">
        <span class="brand__dot"></span>
        <span class="brand__name">Varolune</span>
      </div>
      <div class="purity">100% <span class="purity__script">Pure</span></div>
      <div class="origin">MOROCCAN</div>
      <div class="product">Argan Oil</div>
      <div class="uses">Face, Body &amp; Hair</div>
      <div class="ingredient">Ingredient: Argania Spinosa (Argan) Kernel Oil</div>
    </div>
    <div class="botanical" role="img" aria-label="Botanical drawing of an argan branch with leaves and fruits"></div>
    <div class="footer">
      <span class="footer__web">www.varolune.com</span>
      <span class="footer__volume">50 mL</span>
    </div>
  </section>

</main>
</body>
</html>
```